bottle label/ product label for smoothies (ultra fresh)

Please create a bottle label for our smoothies for retail distribution.
It's important that the following key features are clearly stated:

Ultra-fresh

Handmade

No preservatives

Not heat-treated

No added sugar

The base of the product label should be transparent, so that the color and content of the smoothie can be seen clearly.

We are a young, dynamic company. Our values are honesty, ultra-freshness, and authenticity — and we are the only ones producing this type of product in our country. We are positioned in the premium segment.

Design style: Modern, clean, and natural — but not playful or childish.

Example product: Kelu Kelu (Mango, Pineapple, Lemon, Passion Fruit, Orange)

Wenn du möchtest, kann ich auch gleich einen konkreten Vorschlag für das Etikettendesign auf Englisch oder einen Entwurfstext für das Label selbst erstellen. Sag einfach Bescheid!

Target Market(s)

trade - convenience

Industry/Entity Type

trade

Font styles to use
Sans Serif

Requirements
Must have
• sales- features: Ultra-fresh Handmade No preservatives Not heat-treated No added sugar

```html
<!DOCTYPE html>
<html lang="en">
<head>
<meta charset="utf-8">
<title>Kelu Kelu – Smoothie Label</title>
<link rel="stylesheet" href="https://fonts.googleapis.com/css2?family=Montserrat:wght@400;700&display=swap">
<style>
  :root {
    --backdrop: #f4f3f1;
    --smoothie-light: #fbc43a;
    --smoothie-mid: #f6b21f;
    --smoothie-deep: #eea312;
    --ink: #1b1a18;
  }
  * { margin: 0; padding: 0; box-sizing: border-box; }
  html, body {
    width: 1200px;
    height: 1200px;
    overflow: hidden;
    background: var(--backdrop);
  }
  .canvas {
    position: relative;
    width: 1200px;
    height: 1200px;
    display: flex;
    align-items: center;
    justify-content: center;
  }
  .label {
    position: relative;
    width: 620px;
    height: 1140px;
    background: linear-gradient(90deg, var(--smoothie-deep) 0%, var(--smoothie-light) 35%, var(--smoothie-mid) 70%, var(--smoothie-deep) 100%);
    font-family: "Montserrat", sans-serif;
    color: var(--ink);
    overflow: hidden;
  }
  .fruit-pattern {
    position: absolute;
    inset: 0;
    background: radial-gradient(ellipse at 50% 45%, rgba(255, 236, 170, 0.35) 0%, rgba(255, 236, 170, 0) 70%);
  }
  .brand-name {
    position: absolute;
    top: 70px;
    left: 0;
    right: 0;
    text-align: center;
    font-size: 168px;
    font-weight: 400;
    line-height: 1.3;
    letter-spacing: 0.06em;
    color: var(--ink);
  }
  .features {
    position: absolute;
    top: 610px;
    left: 95px;
    list-style: none;
    font-size: 36px;
    font-weight: 400;
    line-height: 1.55;
    letter-spacing: 0.02em;
  }
  .features li::before {
    content: "•";
    display: inline-block;
    width: 34px;
    font-size: 26px;
    vertical-align: 4px;
  }
  .divider {
    position: absolute;
    top: 910px;
    left: 0;
    right: 0;
    height: 2px;
    background: var(--ink);
  }
  .ingredients {
    position: absolute;
    top: 940px;
    left: 0;
    right: 0;
    text-align: center;
    font-size: 15.5px;
    font-weight: 700;
    letter-spacing: 0.04em;
    text-transform: uppercase;
  }
</style>
</head>
<body>
  <main class="canvas">
    <section class="label">
      <div class="fruit-pattern" role="img" aria-label="Faint outline pattern of mango, pineapple, lemon, passion fruit and orange over the visible smoothie"></div>
      <h1 class="brand-name">KELU<br>KELU</h1>
      <ul class="features">
        <li>Ultra-fresh</li>
        <li>Handmade</li>
        <li>No preservatives</li>
        <li>Not heat-treated</li>
        <li>No added sugar</li>
      </ul>
      <div class="divider"></div>
      <p class="ingredients">Mango · Pineapple · Lemon · Passion Fruit · Orange</p>
    </section>
  </main>
</body>
</html>
```